Lantern over the Harbor ~ A Widening Passage for Writers

My book is called “Lantern over the Harbor.” Its subtitle is “A Widening Passage for Writers.” It is a book about being a poet, writing poetry, and the ways in which poets are connected to both society and the central energy of the Universe. I want the cover design to be abstract and impressionistic. A suggestion of fireworks or a starburst would be a plus. To be consistent with the 3 other books I have published, I want the font for the title, as well as my name (Dorothea Quillbrake) to be Papyrus. The subtitle font can be something more plain and sans serif, like Arial or Franklin Gothic Book, probably in italics. As for color, I definitely want pale gold (angelic). Possible other complimentary colors could be either light or dark shades of gray, turquoise, rose, rust or red. I'm attaching the back cover text and also three pages from inside the book that have line drawings, to give an example of the interior artwork.
Updates

Forgot to mention: My book is a paperback. Its size will be 8.5" high and 5.5" wide. I'm self-publishing it, and it will be printed by Halvern Printworks in Nebraska, USA. It has 104 pages. I think you need the number of pages, in order to make the spine of the book the correct width.

Target Market(s)

My target market is people who write poetry or are interested in how poetry is written.

Industry/Entity Type

Poetry

Font styles to use
Sans Serif
Other font styles liked:
• Papyrus for the front cover. Arial or another sans serif font on the back cover.

Colors

Designer to choose colors to be used in the design.

Requirements
Must have
• My book cover needs to be inspiring and uplifting, as well as abstract and impressionistic, with kind of a "New Age" feel. I don't want anything that looks rigid and scholarly.
Nice to have
• The book talks about the connection poets have to the Universe and the Creative Energy at the center of everything. The cover should convey that Energy.
Should not have
• My cover should not be realistic, logical or straight-laced. I want something that feels free, imaginative and unfettered.

```html
<!DOCTYPE html>
<html lang="en">
<head>
<meta charset="utf-8">
<title>Lantern over the Harbor – Cover Wrap</title>
<link href="https://fonts.googleapis.com/css2?family=Macondo&family=Libre+Franklin:ital,wght@1,400&display=swap" rel="stylesheet">
<style>
  :root {
    --gold-pale: #f6e7b8;
    --gold: #e9b45a;
    --rust: #d98a2e;
    --teal: #5e8a8c;
    --teal-deep: #2f4f55;
    --slate: #3a4a4c;
    --title-red: #6e1410;
    --ink: #111111;
    --paper: #ffffff;
  }
  html, body {
    margin: 0;
    padding: 0;
    width: 1200px;
    height: 904px;
    overflow: hidden;
    background: var(--slate);
  }
  .cover-wrap {
    position: relative;
    width: 1200px;
    height: 904px;
    overflow: hidden;
  }
  .cover-art {
    position: absolute;
    inset: 0;
    background:
      radial-gradient(circle at 800px 400px, rgba(255,250,225,0.95) 0, rgba(250,225,150,0.75) 90px, rgba(240,190,90,0) 300px),
      radial-gradient(ellipse 520px 420px at 330px 260px, rgba(246,231,184,0.9), rgba(233,180,90,0.55) 60%, rgba(233,180,90,0) 100%),
      radial-gradient(ellipse 420px 300px at 300px 520px, rgba(217,138,46,0.7), rgba(217,138,46,0) 100%),
      radial-gradient(ellipse 500px 520px at 1080px 620px, rgba(47,79,85,0.9), rgba(47,79,85,0) 100%),
      linear-gradient(180deg, rgba(0,0,0,0) 60%, rgba(30,45,48,0.55) 100%),
      linear-gradient(100deg, var(--gold-pale) 0%, var(--gold) 35%, #c9b88f 55%, var(--teal) 80%, var(--teal-deep) 100%);
  }
  .title-back, .title-front, .spine-title, .spine-author, .author-front {
    font-family: "Macondo", "Papyrus", fantasy;
    font-weight: 400;
    margin: 0;
    position: absolute;
    white-space: nowrap;
  }
  .subtitle, .back-copy, .author-name-back, .author-bio {
    font-family: "Libre Franklin", "Franklin Gothic Book", Arial, sans-serif;
    font-style: italic;
    font-weight: 400;
    margin: 0;
    position: absolute;
    color: var(--ink);
  }

  /* Back cover */
  .title-back {
    left: 123px;
    top: 40px;
    font-size: 50px;
    line-height: 56px;
    color: var(--title-red);
  }
  .title-back .line-2 { display: block; padding-left: 116px; }
  .subtitle-back {
    left: 44px;
    width: 495px;
    top: 175px;
    font-size: 20px;
    text-align: center;
  }
  .back-copy {
    left: 44px;
    top: 236px;
    width: 495px;
    font-size: 15.3px;
    line-height: 21.1px;
    text-align: justify;
  }
  .back-copy p { margin: 0; }
  .author-photo {
    position: absolute;
    left: 43px;
    top: 626px;
    width: 160px;
    height: 159px;
    background: var(--paper);
  }
  .author-name-back {
    left: 224px;
    top: 620px;
    font-size: 25px;
  }
  .author-bio {
    left: 224px;
    top: 661px;
    width: 315px;
    font-size: 15.3px;
    line-height: 21.1px;
    text-align: justify;
  }

  /* Spine */
  .spine-title, .spine-author {
    left: 597px;
    transform-origin: 0 0;
    transform: rotate(90deg) translateY(-50%);
    font-size: 26px;
    line-height: 34px;
  }
  .spine-title { top: 158px; color: var(--title-red); }
  .spine-author { top: 662px; color: var(--paper); }

  /* Front cover */
  .title-front {
    left: 656px;
    top: 136px;
    width: 520px;
    color: var(--ink);
  }
  .title-front .line {
    display: block;
    white-space: nowrap;
  }
  .title-front .line-1 {
    font-size: 68px;
    line-height: 72px;
  }
  .title-front .line-echo {
    font-size: 50px;
    line-height: 54px;
    padding-left: 180px;
    color: var(--title-red);
  }
  .title-front .line-2 {
    font-size: 68px;
    line-height: 72px;
    padding-left: 108px;
  }
  .subtitle-front {
    left: 660px;
    width: 485px;
    top: 603px;
    font-size: 31px;
    text-align: center;
  }
  .author-front {
    left: 660px;
    width: 485px;
    top: 805px;
    font-size: 37px;
    text-align: center;
    color: var(--paper);
  }
</style>
</head>
<body>
<div class="cover-wrap">
  <div class="cover-art" role="img" aria-label="Abstract impressionistic starburst of golden fireworks sparks over warm gold and rust clouds fading into teal night sky"></div>

  <section class="back-cover">
    <h2 class="title-back">Lantern over the<span class="line-2">Harbor</span></h2>
    <p class="subtitle subtitle-back">A Widening Passage for Writers</p>
    <div class="back-copy">
      <p>more wholesome, more unified experience of life than that which presently surrounds us.</p>
      <p>Tremendous Energy surges around us, snapping and crackling in the night of our confusion. We need to scoop the lightning up in our hands and toss it back at the sky. We need to touch the great cycles beyond our control and experience. Creation governs these cycles. Growth is part of these cycles. So are Reverence and Change. It is time to surrender ourselves to these currents flowing through our consciousness and, with our wrists spanning the continents, become creatures of the Universe once more.</p>
      <p>Creation is always possible. That fact is the essence of Poetic Vision. We have the power, if we so choose, to plant a new the scorched land.</p>
      <p>Liberation is always possible. Bruised as we are, we can still fly. There is always the Phoenix for hope.</p>
    </div>
    <div class="author-photo" role="img" aria-label="Author photo placeholder"></div>
    <p class="author-name-back">Dorothea Quillbrake</p>
    <p class="author-bio">Lorem ipsum dolor sit amet, consectetur adipiscing elit, sed do eiusmod tempor incididunt ut labore et dolore magna aliqua. Quis ipsum suspendisse ultrices gravida. Risus commodo viverra maecenas accumsan lacus vel facilisis.</p>
  </section>

  <section class="spine">
    <p class="spine-title">Lantern over the Harbor</p>
    <p class="spine-author">Dorothea Quillbrake</p>
  </section>

  <section class="front-cover">
    <h1 class="title-front"><span class="line line-1">Lantern over the</span><span class="line line-echo">over the</span><span class="line line-2">Harbor</span></h1>
    <p class="subtitle subtitle-front">A Widening Passage for Writers</p>
    <p class="author-front">Dorothea Quillbrake</p>
  </section>
</div>
</body>
</html>
```